Cash For clothes textile recycling company leaflet design

We need flyer design for textile recycling company called RK BRIGHTMEADOW LTD , we pay cash for peoples unwanted clothes and helping enviroment by moving used unwanted clothing to other countries in need, we are not charity company,as we pay money for people for their unwanted clothing. We would like to see designs that use yellow pink and bright green collors (more summer themes) you can use one or few logos we have uploaded

Industry/Entity Type

Textile

Font styles to use
Decorative

Colors
fbee3d
e34197
33a6d7
abd036
a54499
fece3e

Requirements
Nice to have
• you can play with logos, everything can be colourful, more soft colours, people shouldn't be pushed away from reading the leaflet, some sort of logos with smiles or so can appear as well
Should not have
• no big notes or cash pictures (can be something small) nothing dark or sad looking.

```html
<!DOCTYPE html>
<html lang="en">
<head>
<meta charset="utf-8">
<title>RK Brightmeadow Ltd – Cash for Clothes Leaflet</title>
<link rel="stylesheet" href="https://fonts.googleapis.com/css2?family=Open+Sans:wght@400;600;700;800&display=swap">
<style>
  :root {
    --page: #f1efea;
    --grass-dark: #1f3a14;
    --grass-mid: #2f5a1f;
    --grass-light: #3e6e28;
    --white: #ffffff;
    --orange: #e8782c;
    --yellow: #fbe41e;
    --blue: #1ea3c9;
    --red: #e02a2a;
    --tick-green: #2e9a34;
    --cross-red: #c8262b;
    --badge-green: #3d9a35;
  }
  * { margin: 0; padding: 0; box-sizing: border-box; }
  html, body {
    width: 1200px; height: 1018px; overflow: hidden;
    background: var(--page);
    font-family: "Open Sans", Arial, sans-serif;
  }
  .flyer {
    position: absolute; left: 64px; top: 92px;
    width: 1076px; height: 820px; overflow: hidden;
    color: var(--white);
  }
  .grass {
    position: absolute; inset: 0;
    background: radial-gradient(ellipse at 50% 45%, var(--grass-light), var(--grass-mid) 55%, var(--grass-dark));
  }
  .marks { position: absolute; inset: 0; }
  .title {
    position: absolute; left: 0; right: 0; top: 22px;
    text-align: center; font-size: 82px; font-weight: 700; letter-spacing: -1.5px; line-height: 1;
  }
  .title .suffix { font-weight: 400; }
  .reg {
    position: absolute; left: 0; right: 0; top: 113px;
    text-align: center; font-size: 18px; font-weight: 700; color: var(--orange); letter-spacing: 0.3px;
  }
  .clothes {
    position: absolute; left: 352px; top: 145px; width: 300px; height: 330px;
    border-radius: 48% 52% 46% 54%;
    background: radial-gradient(circle at 45% 40%, #f7e31c 0 28%, #e9512a 45%, #7fb33c 62%, #9b4fa0 78%, transparent 80%);
  }
  .accept { position: absolute; left: 70px; top: 195px; }
  .accept h2 { font-size: 32px; font-weight: 700; margin-bottom: 34px; }
  .accept ul { list-style: none; font-size: 26px; font-weight: 600; line-height: 33px; }
  .accept li { position: relative; padding-left: 26px; }
  .accept li::before { content: "•"; position: absolute; left: 2px; }
  .reject { position: absolute; left: 748px; top: 160px; }
  .reject h2 { font-size: 32px; font-weight: 700; line-height: 31px; margin-bottom: 6px; }
  .reject ul { list-style: none; font-size: 20px; font-weight: 700; line-height: 22.5px; }
  .reject li { position: relative; padding-left: 26px; }
  .reject li::before { content: "•"; position: absolute; left: 6px; }
  .offer {
    position: absolute; left: 0; right: 0; top: 474px;
    text-align: center; font-weight: 700; line-height: 1.05;
  }
  .offer .pay { font-size: 32px; }
  .offer .call { font-size: 31px; margin-top: 2px; }
  .offer .phone { font-size: 56px; color: var(--yellow); }
  .offer .mail { font-size: 31px; }
  .offer .email { color: var(--yellow); }
  .offer .body { font-size: 30px; line-height: 33.5px; font-weight: 700; margin-top: 4px; }
  .hl-blue { color: var(--blue); }
  .hl-red { color: var(--red); }
  .badge {
    position: absolute; background: var(--white);
    display: flex; align-items: center; justify-content: center; gap: 10px;
    font-weight: 800; color: var(--badge-green);
  }
  .badge-loop { left: 0; top: 610px; width: 185px; height: 181px; flex-direction: column; font-size: 24px; }
  .badge-thread { left: 868px; top: 646px; width: 208px; height: 133px; font-size: 30px; }
  .dot { width: 40px; height: 40px; border-radius: 50%; background: var(--badge-green); flex: none; }
</style>
</head>
<body>
  <main class="flyer">
    <div class="grass" role="img" aria-label="Photo of a green lawn filling the leaflet background"></div>

    <svg class="marks" width="1076" height="820" viewBox="0 0 1076 820" aria-hidden="true">
      <polygon class="tick" points="18,340 95,300 150,380 330,190 355,230 150,465" fill="var(--tick-green)"/>
      <g class="cross" stroke="var(--cross-red)" stroke-width="42" stroke-linecap="butt">
        <line x1="730" y1="160" x2="1030" y2="420"/>
        <line x1="1000" y1="130" x2="770" y2="440"/>
      </g>
    </svg>

    <h1 class="title">RK BRIGHTMEADOW <span class="suffix">LTD</span></h1>
    <p class="reg">REGISTERED IN ENGLAND &amp; WALES COMPANY NUMBER: 08316472</p>

    <div class="clothes" role="img" aria-label="Photo of a colourful pile of clothes with a yellow T-shirt and a red trainer"></div>

    <section class="accept">
      <h2>WE ACCEPT:</h2>
      <ul>
        <li>Any clean dry<br>clothing;</li>
        <li>Paired shoes;</li>
        <li>Belts;</li>
        <li>Handbags;</li>
      </ul>
    </section>

    <section class="reject">
      <h2>WE DO NOT<br>ACCEPT:</h2>
      <ul>
        <li>Bad quality, wet, stained,<br>mouldy or ripped items;</li>
        <li>Used socks, underwear;</li>
        <li>Quits, duvets, pillows;</li>
        <li>Bedding, curtains;</li>
        <li>Carpets, mats, rugs;</li>
        <li>Books;</li>
        <li>CDs, DVDs, audio<br>and video tapes;</li>
        <li>Glass, metal, wood.</li>
      </ul>
    </section>

    <section class="offer">
      <p class="pay">WE WILL PAY 55P PER KG</p>
      <p class="call">just call <span class="phone">07700900318</span></p>
      <p class="mail">or email <span class="email">brightmeadow2303@mailbox.example</span></p>
      <p class="body">to arrange collection, and our helpful and<br>friendly staff will make sure that <span class="hl-blue">your<br>unwanted clothing</span> will be collected<br>as soon as possible, and <span class="hl-red">pay you cash<br>straight away!</span></p>
    </section>

    <div class="badge badge-loop"><span class="dot"></span>Loop Again</div>
    <div class="badge badge-thread">Threadway</div>
  </main>
</body>
</html>
```